Business card design needed

Marketing Communications

Target Market(s)

prospective clients in the marketing communications industry

Industry/Entity Type

Business

Contact Information for Business Card

marel tusk
Marketing Communications
lorapen@tidewire.com
0493 518274

Logo Text

marel tusk

Logo styles of interest
Abstract Logo
Requirements
Must have
• An appropriate abstract logo. only a one or two colour design
Nice to have
• Logo to portray the growth of a marketing brief
Should not have
• no more than two colours maximum

```html
<!DOCTYPE html>
<html lang="en">
<head>
<meta charset="utf-8">
<title>Marel Tusk — Business Card</title>
<link rel="stylesheet" href="https://fonts.googleapis.com/css2?family=Poiret+One&family=Questrial&display=swap">
<style>
  :root {
    --page: #ffffff;
    --card: #2a2a2a;
    --accent: #dfe33c;
    --name-highlight: #ffffff;
    --subtitle: #c9c9c9;
    --field-light: #ffffff;
    --field-shade: #cfcfcf;
    --field-text: #111111;
  }
  html, body {
    margin: 0;
    padding: 0;
    width: 1200px;
    height: 1000px;
    overflow: hidden;
    background: var(--page);
  }
  .canvas {
    position: relative;
    width: 1200px;
    height: 1000px;
  }
  .card {
    position: absolute;
    left: 66px;
    top: 195px;
    width: 1062px;
    height: 614px;
    background: var(--card);
    box-shadow: 0 6px 18px rgba(0,0,0,0.25);
  }
  .band {
    position: absolute;
    left: 0;
    width: 100%;
    height: 22px;
    background: var(--accent);
  }
  .band--top { top: 0; }
  .band--bottom { bottom: 0; }
  .identity {
    position: absolute;
    top: 190px;
    left: 0;
    width: 100%;
    text-align: center;
  }
  .name {
    margin: 0;
    font-family: "Poiret One", "Questrial", sans-serif;
    font-weight: 400;
    font-size: 56px;
    letter-spacing: 3px;
    line-height: 1;
    color: var(--accent);
    text-transform: uppercase;
  }
  .name .highlight { color: var(--name-highlight); }
  .role {
    margin: 6px 0 0;
    font-family: "Questrial", sans-serif;
    font-size: 44px;
    letter-spacing: 2px;
    line-height: 1.1;
    color: var(--subtitle);
  }
  .contact {
    position: absolute;
    top: 345px;
    left: 274px;
    width: 508px;
    margin: 0;
    padding: 0;
    list-style: none;
  }
  .contact__field {
    height: 54px;
    margin-bottom: 24px;
    border-radius: 27px;
    background: linear-gradient(to bottom, var(--field-shade) 0%, var(--field-light) 30%, var(--field-light) 70%, var(--field-shade) 100%);
    font-family: "Questrial", sans-serif;
    font-size: 34px;
    letter-spacing: 1.5px;
    color: var(--field-text);
    text-align: center;
    line-height: 56px;
  }
</style>
</head>
<body>
  <main class="canvas">
    <section class="card" aria-label="Business card for Marel Tusk">
      <div class="band band--top"></div>
      <div class="identity">
        <h1 class="name">Marel T<span class="highlight">u</span>sk</h1>
        <p class="role">Marketing Communications</p>
      </div>
      <ul class="contact">
        <li class="contact__field">0493 518274</li>
        <li class="contact__field">lorapen@tidewire.com</li>
      </ul>
      <div class="band band--bottom"></div>
    </section>
  </main>
</body>
</html>
```